Calder Pizza - Takeout Menu Design

We are looking for a takeout menu design.
We are looking for a( 5" x 8.5" DOUBLE SIDED) flyer with our available pizza flavors
Must be easy to ready and not "busy"

Must include our logo (attached)
website: www.calderpizza.ca
address:
Fenwick Ridge Plaza
417, 318 9 Avenue SW
and the following details:
Visit our website for our complete appetizer, pasta, salad and catering menu.

Winner of this contest will also be offered to create a few print designs via printhive.

Please do not hesitate to ask any questions.

Target Market(s)

Business / Office clientele

Industry/Entity Type

Pizza place / specializing in corporate orders

Requirements
Must have
• Easy to read
Should not have
• Can not be busy or cluttered

```html
<!DOCTYPE html>
<html lang="en">
<head>
<meta charset="utf-8">
<title>Calder Pizza – Take-Out Menu</title>
<link href="https://fonts.googleapis.com/css2?family=Lato:wght@400;700&family=Permanent+Marker&family=Kaushan+Script&display=swap" rel="stylesheet">
<style>
:root{
  --bg:#ece7e1;
  --red:#c0301f;
  --red-text:#e23b2a;
  --desc:#d6392a;
  --black:#000;
  --white:#fff;
}
*{box-sizing:border-box;margin:0;padding:0}
html,body{width:1200px;height:1200px;overflow:hidden;background:var(--bg);font-family:'Lato',sans-serif}
.menu-side{position:absolute;top:150px;width:530px;height:900px;background:var(--red);overflow:hidden;box-shadow:0 6px 18px rgba(0,0,0,.25)}
.side-front{left:50px}
.side-back{left:620px}
.abs{position:absolute}
.brand-band{left:30px;top:18px;width:470px;height:100px;background:var(--white);border-radius:4px}
.brand-name{left:0;width:530px;top:40px;text-align:center;font-size:46px;letter-spacing:1px;color:var(--black);font-weight:400;line-height:56px}
.brand-dot{display:inline-block;width:14px;height:14px;border-radius:50%;background:var(--red);margin-right:12px;vertical-align:middle}
.board{background:var(--black)}
.classic-board{left:32px;top:142px;width:520px;height:264px;border-radius:24px 0 0 24px}
.special-board{left:-20px;top:421px;width:509px;height:369px;border-radius:0 24px 24px 0}
.photo{border-radius:50%;background:radial-gradient(circle at 45% 45%,#f0a04a 0%,#d5522a 45%,#b83a1e 75%,#e5b06a 92%,#c9883e 100%)}
.photo-top{left:365px;top:107px;width:347px;height:347px}
.photo-bottom{left:-260px;top:406px;width:400px;height:400px}
.heading{font-family:'Permanent Marker',cursive;color:var(--white);font-size:34px;line-height:36px;letter-spacing:1px}
.subheading{font-family:'Kaushan Script',cursive;color:var(--red-text);font-size:22px;line-height:26px}
.size-label{font-family:'Kaushan Script',cursive;color:var(--red-text);font-size:18px;line-height:22px}
.classic-row{font-size:13.5px;line-height:18px;color:var(--white);font-weight:700}
.classic-row .price{position:absolute;top:0;color:var(--red-text);font-weight:400}
.item{color:var(--white)}
.item-name{font-size:13.5px;line-height:16px;font-weight:700;white-space:nowrap}
.item-desc{font-size:8.4px;line-height:10px;color:var(--desc);white-space:nowrap}
.item-price{position:absolute;top:0;font-size:13.5px;line-height:16px;color:var(--white);white-space:nowrap}
.back-board{left:31px;top:14px;width:468px;height:793px;border-radius:22px}
.back-brand{left:300px;top:30px;font-size:25px;line-height:28px;color:var(--white);white-space:nowrap;font-weight:400}
.tax-note{left:0;width:530px;text-align:center;color:var(--white);font-size:10.5px;line-height:12px;font-weight:700}
.address{left:0;width:530px;text-align:center;color:var(--white);font-size:17px;line-height:20px;font-weight:700}
.address svg{vertical-align:-3px;margin-right:8px}
.footer{left:0;width:530px;height:54px;background:var(--black);color:var(--white);text-align:center}
.footer-note{font-size:12.5px;line-height:16px;margin-top:8px}
.footer-url{font-size:14px;line-height:18px;letter-spacing:6.5px;font-weight:700;margin-top:3px}
</style>
</head>
<body>

<section class="menu-side side-front">
  <div class="abs brand-band"></div>
  <div class="abs brand-name"><span class="brand-dot"></span>CALDER PIZZA</div>

  <div class="abs board classic-board"></div>
  <div class="abs photo photo-top" role="img" aria-label="Photo of a pepperoni and tomato pizza"></div>

  <div class="abs heading" style="left:62px;top:160px">CLASSIC</div>
  <div class="abs subheading" style="left:62px;top:197px">Take-Out Pizza</div>
  <div class="abs size-label" style="left:257px;top:200px">8"</div>
  <div class="abs size-label" style="left:316px;top:200px">13"</div>

  <div class="abs classic-row" style="left:61px;top:230px;width:240px">Pepperoni &amp; Ham<span class="price" style="left:173px">$12.99</span><span class="price" style="left:230px">$30.95</span></div>
  <div class="abs classic-row" style="left:61px;top:249.5px;width:240px">Ham &amp; Mushroom<span class="price" style="left:173px">$12.99</span><span class="price" style="left:230px">$30.95</span></div>
  <div class="abs classic-row" style="left:61px;top:269px;width:240px">Beef &amp; Onion<span class="price" style="left:173px">$13.49</span><span class="price" style="left:230px">$32.95</span></div>
  <div class="abs classic-row" style="left:61px;top:288.5px;width:240px">Cheese<span class="price" style="left:173px">$11.99</span><span class="price" style="left:230px">$29.95</span></div>
  <div class="abs classic-row" style="left:61px;top:308px;width:240px">Pepperoni &amp; Mushroom<span class="price" style="left:173px">$12.99</span><span class="price" style="left:230px">$30.95</span></div>
  <div class="abs classic-row" style="left:61px;top:327.5px;width:240px">Pepperoni<span class="price" style="left:173px">$11.99</span><span class="price" style="left:230px">$29.95</span></div>
  <div class="abs classic-row" style="left:61px;top:347px;width:240px">Hawaiian<span class="price" style="left:173px">$12.99</span><span class="price" style="left:230px">$30.95</span></div>
  <div class="abs classic-row" style="left:61px;top:366.5px;width:240px">Beef &amp; Mushroom<span class="price" style="left:173px">$13.49</span><span class="price" style="left:230px">$32.95</span></div>

  <div class="abs board special-board"></div>
  <div class="abs photo photo-bottom" role="img" aria-label="Photo of a salami, olive and onion pizza"></div>

  <div class="abs heading" style="left:153px;top:439px">SPECIALTY</div>
  <div class="abs subheading" style="left:153px;top:476px">Take-Out Pizza</div>
  <div class="abs size-label" style="left:373px;top:479px">8"</div>
  <div class="abs size-label" style="left:432px;top:479px">13"</div>

  <div class="abs item" style="left:153px;top:511px"><div class="item-name">All Meat</div><div class="item-desc">Pepperoni, Beef &amp; Smoked Ham &amp; Bacon</div><span class="item-price" style="left:196px">$14.99</span><span class="item-price" style="left:253px">$35.95</span></div>
  <div class="abs item" style="left:153px;top:555px"><div class="item-name">Double Pepperoni</div><div class="item-desc">Loads of Pepperoni</div><span class="item-price" style="left:196px">$13.49</span><span class="item-price" style="left:253px">$32.95</span></div>
  <div class="abs item" style="left:153px;top:599px"><div class="item-name">Hot Honey Pepperoni</div><div class="item-desc">Double Pepperoni and drizzled with Hot Honey</div><span class="item-price" style="left:196px;top:5px">$14.49</span><span class="item-price" style="left:253px;top:5px">$34.95</span></div>
  <div class="abs item" style="left:153px;top:643px"><div class="item-name">Hawaiian Heat</div><div class="item-desc">Smoked Ham, Pineapple and Banana Peppers</div><span class="item-price" style="left:196px;top:5px">$13.49</span><span class="item-price" style="left:253px;top:5px">$32.95</span></div>
  <div class="abs item" style="left:153px;top:687px"><div class="item-name">Four Cheese</div><div class="item-desc">Mozzarella, Feta, Romano and Cheddar Cheese</div><span class="item-price" style="left:196px;top:5px">$13.49</span><span class="item-price" style="left:253px;top:5px">$32.95</span></div>
  <div class="abs item" style="left:153px;top:731px"><div class="item-name">Montreal</div><div class="item-desc">Pepperoni &amp; Double Smoked Bacon</div><span class="item-price" style="left:196px;top:14px">$13.49</span><span class="item-price" style="left:253px;top:14px">$32.95</span></div>

  <div class="abs tax-note" style="top:801px">GST not included</div>
  <div class="abs address" style="top:818px"><svg width="14" height="18" viewBox="0 0 14 18" aria-hidden="true"><path d="M7 0C3.1 0 0 3.1 0 7c0 5 7 11 7 11s7-6 7-11c0-3.9-3.1-7-7-7z" fill="#fff"/><circle cx="7" cy="7" r="2.6" fill="#c0301f"/></svg>Fenwick Ridge Plaza 417, 318 9 Avenue SW</div>
  <div class="abs footer" style="top:846px">
    <p class="footer-note">Visit our website for our complete appetizer, pasta, salad and catering menu.</p>
    <p class="footer-url">www.calderpizza.ca</p>
  </div>
</section>

<section class="menu-side side-back">
  <div class="abs board back-board"></div>
  <div class="abs heading" style="left:59px;top:26px">SPECIALTY</div>
  <div class="abs subheading" style="left:59px;top:62px">Take-Out Pizza</div>
  <div class="abs back-brand"><span class="brand-dot" style="width:9px;height:9px;margin-right:7px;background:var(--white)"></span>CALDER PIZZA</div>
  <div class="abs size-label" style="left:386px;top:64px">8"</div>
  <div class="abs size-label" style="left:445px;top:64px">13"</div>

  <div class="abs item" style="left:62px;top:91px"><div class="item-name">Montreal Heat</div><div class="item-desc">Pepperoni, Double Smoked Bacon &amp; Banana Peppers</div><span class="item-price" style="left:309px">$13.99</span><span class="item-price" style="left:359px">$33.95</span></div>
  <div class="abs item" style="left:62px;top:127px"><div class="item-name">Supreme</div><div class="item-desc">Pepperoni, Mushrooms &amp; Green Peppers</div><span class="item-price" style="left:309px">$13.49</span><span class="item-price" style="left:359px">$32.95</span></div>
  <div class="abs item" style="left:62px;top:162px"><div class="item-name">Canadian</div><div class="item-desc">Pepperoni, Mushrooms &amp; Ham</div><span class="item-price" style="left:309px">$13.49</span><span class="item-price" style="left:359px">$32.95</span></div>
  <div class="abs item" style="left:62px;top:197px"><div class="item-name">BBQ Chicken</div><div class="item-desc">Chicken Breast, Hickory BBQ Sauce &amp; Red Onions.</div><span class="item-price" style="left:309px">$13.99</span><span class="item-price" style="left:359px">$33.95</span></div>
  <div class="abs item" style="left:62px;top:232px"><div class="item-name">BBQ Chicken Plus</div><div class="item-desc" style="margin-top:4px">Chicken Breast, Hickory BBQ Sauce, Red Onions &amp; Cilantro</div><span class="item-price" style="left:309px;top:3px">$14.79</span><span class="item-price" style="left:359px;top:3px">$34.95</span></div>
  <div class="abs item" style="left:62px;top:273px"><div class="item-name">Spicy BBQ Chicken</div><div class="item-desc">Chicken Breast, Hickory BBQ Sauce, Red Onions &amp; Banana Peppers</div><span class="item-price" style="left:309px">$14.49</span><span class="item-price" style="left:359px">$35.95</span></div>
  <div class="abs item" style="left:62px;top:308px"><div class="item-name">Sweet Chili Chicken</div><div class="item-desc">Chicken Breast, Pineapple, Red Onions &amp; Sweet Chili Sauce</div><span class="item-price" style="left:309px">$14.49</span><span class="item-price" style="left:359px">$35.95</span></div>
  <div class="abs item" style="left:62px;top:343px"><div class="item-name">Chicken Club</div><div class="item-desc">Chicken Breast, Double Smoked Bacon, Red Onions and Tomatoes</div><span class="item-price" style="left:309px">$14.79</span><span class="item-price" style="left:359px">$35.95</span></div>
  <div class="abs item" style="left:62px;top:378px"><div class="item-name">Athenean</div><div class="item-desc">Chicken Breast, Spinach, Feta Cheese and Tomato</div><span class="item-price" style="left:309px">$14.49</span><span class="item-price" style="left:359px">$34.95</span></div>
  <div class="abs item" style="left:62px;top:413px"><div class="item-name">Greek Supreme</div><div class="item-desc">Chicken Breast, Feta Cheese, Tomato, Green Pepper, Red Onions &amp; Black Olives</div><span class="item-price" style="left:309px">$14.99</span><span class="item-price" style="left:359px">$35.95</span></div>
  <div class="abs item" style="left:62px;top:448px"><div class="item-name">Mediterranean Chicken</div><div class="item-desc">Seasoned Chicken Breast, Tomatoes, Red Onions and Feta Cheese</div><span class="item-price" style="left:309px;top:3px">$14.79</span><span class="item-price" style="left:359px;top:3px">$35.95</span></div>
  <div class="abs item" style="left:62px;top:484px"><div class="item-name">Original Spinach</div><div class="item-desc">Spinach &amp; Feta Cheese</div><span class="item-price" style="left:309px;top:5px">$13.49</span><span class="item-price" style="left:359px;top:5px">$32.95</span></div>
  <div class="abs item" style="left:62px;top:519px"><div class="item-name">Zeus</div><div class="item-desc">Spinach, Feta Cheese and Tomatoes</div><span class="item-price" style="left:309px">$13.95</span><span class="item-price" style="left:359px">$33.95</span></div>
  <div class="abs item" style="left:62px;top:554px"><div class="item-name">Greek</div><div class="item-desc">Feta Cheese, Tomato, Green Peppers, Red Onions and Black Olives</div><span class="item-price" style="left:309px">$13.99</span><span class="item-price" style="left:359px">$33.95</span></div>
  <div class="abs item" style="left:62px;top:589px"><div class="item-name">Vegetarian</div><div class="item-desc">Mushrooms, Tomatoes, Green Peppers and Black Olives</div><span class="item-price" style="left:309px">$13.49</span><span class="item-price" style="left:359px">$32.95</span></div>
  <div class="abs item" style="left:62px;top:624px"><div class="item-name">Veggie Delight</div><div class="item-desc">Mushrooms, Tomatoes, Green Peppers, Black Olives &amp; Onions</div><span class="item-price" style="left:309px">$13.95</span><span class="item-price" style="left:359px">$33.95</span></div>
  <div class="abs item" style="left:62px;top:659px"><div class="item-name">Deluxe</div><div class="item-desc">Pepperoni, Mushrooms, Ham, Tomatoes, Green Peppers and Red Onions</div><span class="item-price" style="left:309px">$14.49</span><span class="item-price" style="left:359px">$34.95</span></div>
  <div class="abs item" style="left:62px;top:692px"><div class="item-name">Calder Special</div><div class="item-desc">Peperoni, Mushrooms, Ham, Green Peppers and Black Olives</div><span class="item-price" style="left:309px">$14.49</span><span class="item-price" style="left:359px">$34.95</span></div>
  <div class="abs item" style="left:62px;top:727px"><div class="item-name">Dill Pickle</div><div class="item-desc">Crispy Dill Pickles, Fresh Dill with our cream based garlic sauce.<br>Served with our without bacon.</div><span class="item-price" style="left:211px;top:2px">$13.49&nbsp; $32.95 &nbsp;/&nbsp; $14.49&nbsp; $35.95</span></div>
  <div class="abs item" style="left:62px;top:772px"><div class="item-name">BBQ Pulled Pork</div><div class="item-desc">Pulled Pork, Red Onions, Red Peppers and Cilantro.</div><span class="item-price" style="left:309px">$14.49</span><span class="item-price" style="left:357px">$35.95</span></div>

  <div class="abs tax-note" style="top:810px">GST not included</div>
  <div class="abs address" style="top:824px"><svg width="14" height="18" viewBox="0 0 14 18" aria-hidden="true"><path d="M7 0C3.1 0 0 3.1 0 7c0 5 7 11 7 11s7-6 7-11c0-3.9-3.1-7-7-7z" fill="#fff"/><circle cx="7" cy="7" r="2.6" fill="#c0301f"/></svg>Fenwick Ridge Plaza 417, 318 9 Avenue SW</div>
  <div class="abs footer" style="top:849px;height:51px">
    <p class="footer-note" style="margin-top:6px">Visit our website for our complete appetizer, pasta, salad and catering menu.</p>
    <p class="footer-url">www.calderpizza.ca</p>
  </div>
</section>

</body>
</html>
```